new Crestline Bug Guard Flyer 8.5"x11"

We need a new flyer for our pest control company. We need it to be themed like our truck wrap. We have also attached is our old flyer.
The Best Defense is a Great Offense. Our Bug Guns are Locked, Loaded and Ready for action!
Don't be caught defenseless, Call Crestline Bug Guard today!!
"The Solution to your bug pollution"
www.CrestlineBugguard.example
555-014-8836

add a 10% off coupon code for existing Marlow Property Checks customers

Target Market(s)

Home owners

Industry/Entity Type

Pest Control

Requirements
Must have
• our theme like our truck wrap

```html
<!DOCTYPE html>
<html lang="en">
<head>
<meta charset="utf-8">
<title>Crestline Bug Guard Flyer</title>
<link href="https://fonts.googleapis.com/css2?family=Anton&family=Black+Ops+One&family=Comfortaa:wght@700&family=Andika:wght@400;700&display=swap" rel="stylesheet">
<style>
  :root {
    --page-bg: #f2f2f2;
    --paper: #e4e3e1;
    --paper-light: #eeedeb;
    --navy: #2a4a9e;
    --red: #d8242b;
    --ink: #1a1a1a;
    --white: #ffffff;
    --bug-brown: #9a5a2e;
    --bug-light: #e8d8c4;
  }
  * { margin: 0; padding: 0; box-sizing: border-box; }
  html, body { width: 1200px; height: 1200px; overflow: hidden; background: var(--page-bg); }
  .flyer {
    position: absolute; left: 167px; top: 40px;
    width: 866px; height: 1120px;
    background: radial-gradient(ellipse at 70% 30%, var(--paper-light), var(--paper));
    box-shadow: 0 10px 30px rgba(0,0,0,.18);
    overflow: hidden;
  }
  .band { position: absolute; left: 0; width: 100%; }
  .band-top { top: 0; height: 150px; }
  .band-bottom { bottom: 0; height: 180px; }
  .brand {
    position: absolute; left: 60px; top: 390px; width: 400px;
    display: flex; align-items: center; gap: 14px;
    font-family: "Anton", sans-serif; font-size: 50px; line-height: 1.05;
    color: var(--ink); text-transform: uppercase;
  }
  .brand-mark { width: 30px; height: 30px; background: var(--navy); flex: none; }
  .headline {
    position: absolute; right: 50px; top: 170px; text-align: right;
    font-family: "Anton", sans-serif; text-transform: uppercase; line-height: .98;
  }
  .headline .line-1 { display: block; color: var(--navy); font-size: 74px; }
  .headline .line-2 { display: block; color: var(--red); font-size: 60px; }
  .bug-art {
    position: absolute; right: 70px; top: 340px; width: 210px; height: 200px;
    border-radius: 50%;
    background: radial-gradient(circle at 45% 45%, var(--bug-light), var(--bug-brown) 75%);
  }
  .tagline {
    position: absolute; left: 60px; top: 568px; width: 760px;
    font-family: "Comfortaa", sans-serif; font-weight: 700; font-size: 28px;
    color: var(--ink); line-height: 1.35;
  }
  .ready {
    position: absolute; left: 60px; top: 650px;
    font-family: "Black Ops One", sans-serif; font-size: 60px; line-height: 1.2; color: var(--red);
  }
  .cta {
    position: absolute; left: 60px; top: 735px; width: 780px;
    font-family: "Andika", sans-serif; font-size: 42px; color: var(--ink); line-height: 1.2;
    white-space: nowrap;
  }
  .cta .name { font-family: "Black Ops One", sans-serif; color: var(--red); font-size: 34px; }
  .phone {
    position: absolute; left: 60px; top: 840px;
    display: flex; align-items: center; gap: 12px;
    font-family: "Andika", sans-serif; font-size: 64px; line-height: 1.2; color: var(--navy);
  }
  .phone svg { width: 40px; height: 40px; }
  .coupon {
    position: absolute; right: 50px; top: 848px; width: 270px;
    border: 3px dashed var(--navy); padding: 8px 12px; text-align: center;
    font-family: "Andika", sans-serif; color: var(--ink); font-size: 17px; line-height: 1.25;
  }
  .coupon .coupon-value {
    display: block; font-family: "Black Ops One", sans-serif; color: var(--red); font-size: 30px;
  }
  .website {
    position: absolute; left: 0; bottom: 42px; width: 100%; text-align: center;
    font-family: "Andika", sans-serif; font-size: 48px; color: var(--white);
  }
</style>
</head>
<body>
  <main class="flyer">
    <svg class="band band-top" viewBox="0 0 866 150" preserveAspectRatio="none" aria-hidden="true">
      <path d="M0 0 H866 V95 C780 95 760 150 700 150 C640 150 600 100 520 100 C380 100 250 120 120 120 C70 120 30 118 0 118 Z" fill="var(--navy)"/>
      <path d="M0 118 C30 118 70 120 120 120 C250 120 380 100 520 100 C600 100 640 150 700 150 C760 150 780 95 866 95" fill="none" stroke="var(--white)" stroke-width="5"/>
    </svg>

    <h1 class="headline">
      <span class="line-1">The Solution To</span>
      <span class="line-2">Your Bug Pollution</span>
    </h1>

    <div class="brand"><span class="brand-mark"></span><span>Crestline Bug Guard</span></div>

    <div class="bug-art" role="img" aria-label="Cartoon bug holding a white flag inside a red crosshair"></div>

    <p class="tagline">The Best Defense is a Great Offense,<br>Our Bug Guns are Locked and Loaded</p>
    <p class="ready">READY FOR ACTION!</p>

    <p class="cta">Don't be caught defenseless,<br>Call <span class="name">CRESTLINE BUG GUARD</span> today!!</p>

    <p class="phone">
      <svg viewBox="0 0 24 24" aria-hidden="true"><path fill="var(--navy)" d="M6.6 10.8a15.1 15.1 0 0 0 6.6 6.6l2.2-2.2a1 1 0 0 1 1-.25 11.4 11.4 0 0 0 3.6.57 1 1 0 0 1 1 1V20a1 1 0 0 1-1 1A17 17 0 0 1 3 4a1 1 0 0 1 1-1h3.5a1 1 0 0 1 1 1c0 1.25.2 2.45.57 3.57a1 1 0 0 1-.25 1z"/></svg>
      555-014-8836
    </p>

    <div class="coupon">
      <span class="coupon-value">10% OFF</span>
      for Marlow Property Checks customers
    </div>

    <svg class="band band-bottom" viewBox="0 0 866 180" preserveAspectRatio="none" aria-hidden="true">
      <path d="M0 180 V60 C50 60 80 16 150 16 C300 16 500 30 700 14 C780 8 830 4 866 0 V180 Z" fill="var(--red)"/>
      <path d="M0 60 C50 60 80 16 150 16 C300 16 500 30 700 14 C780 8 830 4 866 0" fill="none" stroke="var(--white)" stroke-width="5"/>
    </svg>
    <p class="website">www.CrestlineBugguard.example</p>
  </main>
</body>
</html>
```